Web design for online activity booking website

Our activity booking website uTrundle.net is looking outdated and needing a loving revamp on its design and STRUCTURE. it was initially created as a destination guide before we modified the homepage slightly to sell activities. So please DON'T RELY on the current website for your design. Now, the focus is ACTIVITY, while guide/ info should come only as secondary.

In other words, we will be doing something very similar to Wandelo.com (a bit crowded for our liking) and FindMyOuting.com. If you could capture the best essences of both, that would be awesome! Besides, we also like roostly.com's simplicity.

SIMPLE, CLEAN, BRIGHT, USER and MOBILE FRIENDLY please :)

We have a new logo created and some wireframes (a few more in progress) so you know the basic components required in each page. These are just rough ideas so please ignore the ratio/size, colours etc and if you have a better way of arranging or simplifying things, please do so :)

Help us make it a website that everyone would love!

Thank you in advance for your time and artistry.

Target Market(s)

Internet savvy travellers between 18-65

Industry/Entity Type

Tourism

Number of Pages Required

5+ page

Requirements
Must have
• SIMPLE, CLEAN feel, USER and MOBILE FRIENDLY please :)
• See attachments for rough structure. Will also need standard pages such as:
• - About Us
• - Contact Us
• - Wishlist etc
• Message from our developer "designer to keep layers in PSD format accurately so html/css code does not need to lead a mess in photoshop"
Nice to have
• UPDATE: We are so thrilled to receive so many web designs but on the other hand, the submissions are getting too generic and everyone's designs is almost looking identical (many look like they are “borrowed” from existing popular websites). This is making the selection and decision process very difficult.
• So instead of sending us more of the very similar homepage design with minor tweaks (which we can do during handover section anyway), please send us a design of more specific page of our website. Please refer job brief, file no. 5 - Product detail page.
• This will give us better idea of your skills and choose the best as winner to work on the rest of our web pages.
Should not have
• No dark background please

```html
<!DOCTYPE html>
<html lang="en">
<head>
<meta charset="utf-8">
<title>uTrundle – Kite Surf Group Lesson</title>
<link href="https://fonts.googleapis.com/css2?family=Roboto:wght@300;400;500;700&family=Roboto+Condensed:wght@400;700&display=swap" rel="stylesheet">
<style>
:root{
  --orange:#f7901e;
  --orange-dark:#e5780b;
  --magenta:#c5168c;
  --dark:#3b3b3b;
  --darker:#262626;
  --tab:#555555;
  --panel:#f2f2f2;
  --line:#d8d8d8;
  --text:#555555;
  --muted:#8a8a8a;
  --link:#1e88c8;
  --star:#f7901e;
  --white:#ffffff;
}
*{box-sizing:border-box;margin:0;padding:0}
html,body{width:1200px;height:3644px;overflow:hidden}
body{font-family:"Roboto",Arial,sans-serif;color:var(--text);background:var(--white);font-size:13px;line-height:1.5;position:relative}
ul{list-style:none}
h1,h2,h3,h4,h5,h6{font-weight:400}

/* top strip */
.topbar{height:24px;background:var(--darker);color:#ddd;font-size:11px;display:flex;align-items:center;justify-content:space-between;padding:0 112px 0 70px}
.topbar span{margin-right:24px}
.topbar .right span{margin:0 0 0 26px}
.site-header{height:96px;background:var(--dark);display:flex;align-items:center;padding:0 112px 0 70px}
.logo{width:320px;color:var(--white)}
.logo .name{font-size:44px;font-weight:700;line-height:1;display:flex;align-items:center;gap:10px}
.logo .name i{display:inline-block;width:18px;height:18px;border-radius:50%;background:var(--magenta)}
.logo .tag{font-size:8px;letter-spacing:1.5px;color:#bbb;margin-top:4px}
.search{display:flex;gap:18px;margin-left:13px}
.select{width:277px;height:34px;background:var(--white);font-size:11px;color:#444;padding:0 12px;display:flex;align-items:center;justify-content:space-between}
.select:after{content:"";border:5px solid transparent;border-top-color:#444;margin-top:5px}
.go{height:34px;width:90px;background:var(--orange);color:var(--white);font-weight:700;font-size:12px;display:flex;align-items:center;justify-content:center}

/* layout */
.page{display:flex;gap:22px;padding:21px 0 0 58px;height:2880px}
.main{width:758px}
.aside{width:250px}

/* product */
.product{display:flex;gap:24px;height:309px}
.product-photo{width:399px;height:309px;background:linear-gradient(160deg,#2f8fb8 0%,#5fb6d4 55%,#9fd3e0 100%)}
.product-info{flex:1;padding-top:2px}
.product-title{font-family:"Roboto Condensed",sans-serif;font-weight:700;color:var(--magenta);font-size:23px;line-height:1.1}
.duration{font-family:"Roboto Condensed",sans-serif;font-weight:700;font-size:14px;color:#444;margin-top:4px}
.intro{font-size:12.5px;line-height:1.65;color:var(--muted);margin-top:14px}
.rating{border-top:1px solid var(--line);border-bottom:1px solid var(--line);margin-top:10px;padding:9px 0;display:flex;align-items:center;gap:10px;font-size:12px;color:#777}
.stars{display:inline-flex;gap:3px}
.stars svg{width:14px;height:14px;fill:var(--star)}
.price-row{display:flex;justify-content:space-between;align-items:flex-end;margin-top:14px}
.from{font-size:11px;color:var(--muted)}
.price{font-family:"Roboto Condensed",sans-serif;font-size:40px;color:#444;line-height:1}
.price small{font-size:26px;color:var(--muted)}
.btn{background:var(--orange);color:var(--white);font-weight:700;display:flex;align-items:center;justify-content:center;border-radius:2px}
.book{width:168px;height:46px;font-size:19px}

.share{display:flex;align-items:center;gap:9px;margin-top:40px;height:36px}
.share b{font-family:"Roboto Condensed",sans-serif;font-size:19px;color:#444;margin-right:6px}
.share .dot{width:31px;height:31px;border-radius:50%;display:flex;align-items:center;justify-content:center}
.share svg{width:16px;height:16px;fill:none;stroke:#fff;stroke-width:2}

/* tabs */
.tabs{display:flex;background:var(--tab);height:58px;margin-top:18px}
.tabs li{color:var(--white);font-size:15px;display:flex;align-items:center;justify-content:center}
.tabs li.active{background:var(--panel);color:#333}
.tab-panel{background:var(--panel);height:1503px;padding:22px 22px 0;overflow:hidden}
.section-title{font-size:20px;font-weight:400;color:#555;border-bottom:2px solid var(--line);padding-bottom:6px;margin-bottom:16px}
.tab-panel p{font-size:12.5px;line-height:1.75;color:#777;margin-bottom:26px}
.group{font-weight:700;font-size:13px;color:#444;margin:6px 0 6px 20px}
.bullets li{font-size:12.5px;color:#777;line-height:2.1;padding-left:40px;position:relative}
.bullets li:before{content:"";position:absolute;left:24px;top:10px;width:5px;height:5px;border-right:1.5px solid #777;border-top:1.5px solid #777;transform:rotate(45deg)}
.block{margin-top:46px}
.map{height:232px;background:linear-gradient(135deg,#e8e3d6,#d9d6cc 50%,#c9d9c3);border:1px solid #ccc}

/* reviews */
.reviews{margin-top:65px;background:var(--panel);height:785px}
.reviews-head{height:56px;background:var(--dark);color:var(--white);display:flex;align-items:center;justify-content:space-between;padding:0 14px}
.reviews-head h3{font-weight:500;font-size:19px}
.reviews-head h3 small{font-size:12px;font-weight:400}
.filter{display:flex;align-items:center;gap:12px;font-size:10px}
.filter .select{width:150px;height:26px;font-size:9px;color:#888}
.review{margin:0 14px;padding:22px 0 14px;border-bottom:1px solid var(--line);height:163px;position:relative}
.review h4{font-family:"Roboto Condensed",sans-serif;font-weight:700;font-size:22px;color:#333}
.review .stars svg{width:17px;height:17px}
.review .body{font-size:13px;color:#555;margin-top:6px}
.review .by{font-size:10.5px;color:#777;margin-top:2px}
.review .who{font-size:10.5px;color:var(--magenta);font-style:italic}
.review .date{position:absolute;right:8px;top:28px;font-size:12px;color:var(--link)}
.helpful{position:absolute;right:8px;bottom:22px;display:flex;align-items:center;gap:12px;font-size:10.5px;color:#555}
.yes{background:var(--magenta);color:#fff;font-size:10px;padding:3px 10px}
.more-review{width:182px;height:38px;margin:30px auto 0;font-size:14px}

/* aside */
.calendar{background:var(--panel);height:400px}
.cal-head{height:46px;background:var(--orange);color:#fff;font-size:21px;display:flex;align-items:center;justify-content:center}
.step{padding:14px 14px 0;font-size:12px;color:#333}
.step .label{display:flex;align-items:center;gap:8px;font-weight:700}
.num{width:20px;height:20px;border-radius:50%;background:#444;color:#fff;font-size:11px;display:flex;align-items:center;justify-content:center}
.fields{display:flex;gap:8px;margin:8px 0 0 28px;align-items:center}
.mini{height:24px;border:1px solid #ccc;background:#fff;font-size:11px;display:flex;align-items:center;padding:0 6px}
.hint{color:var(--link);font-size:10.5px;font-weight:700;margin:6px 0 0 28px}
.travellers{margin:8px 0 0 28px;font-size:11px}
.travellers div{display:flex;align-items:center;justify-content:space-between;width:150px;margin-bottom:6px}
.divider{border-top:1px solid var(--line);margin:16px 14px 0}
.check{width:212px;height:38px;margin:16px auto 0;font-size:15px}

.aside-reviews{margin-top:14px;background:var(--panel);height:771px;padding-bottom:10px}
.rev-head{height:62px;position:relative}
.rev-head svg{position:absolute;inset:0}
.rev-head span{position:absolute;left:0;right:0;top:12px;text-align:center;color:#fff;font-size:21px}
.mini-review{margin:0 14px;padding:22px 0 14px;border-bottom:1px solid var(--line)}
.mini-review h5{font-family:"Roboto Condensed",sans-serif;font-weight:700;color:var(--magenta);font-size:20px}
.mini-review .stars svg{width:12px;height:12px}
.mini-review p{font-size:12.5px;color:#777;margin-top:6px}
.mini-review .from-line{font-size:10.5px;color:#555;margin-top:10px;line-height:1.5}
.mini-review .from-line em{color:var(--link);font-style:normal}
.see-all{width:148px;height:40px;margin:28px auto 0;font-size:14px}

.offer{margin-top:14px;border:1px solid #e2e2e2;height:248px;position:relative;background:#fff}
.offer-photo{height:150px;background:linear-gradient(180deg,#6a8aa8 0%,#5c6b4a 55%,#3f4a3a 100%)}
.heart{position:absolute;right:8px;top:8px;width:36px;height:36px;background:var(--magenta);border-radius:3px;display:flex;align-items:center;justify-content:center}
.heart svg{width:20px;height:20px;fill:#fff}
.offer-body{padding:12px 12px;font-size:12px;color:#444}
.offer-body .stars svg{width:12px;height:12px}
.offer-foot{display:flex;justify-content:space-between;align-items:flex-end;margin-top:8px}
.offer-foot .count{font-size:11px;color:#777}
.offer-foot .amt{text-align:right;font-size:10px;color:var(--muted);line-height:1}
.offer-foot .amt b{display:block;font-size:22px;color:var(--orange);font-weight:400;margin-top:2px}
.more-offer{width:148px;height:40px;margin:30px auto 0;font-size:14px}

/* footer */
.footer-links{position:absolute;left:0;top:3000px;width:1200px;height:334px;background:#f3f4f6;display:flex;padding:34px 0 0 68px}
.col{width:360px}
.col h6{font-family:"Roboto Condensed",sans-serif;font-size:18px;font-weight:400;color:#333;border-bottom:1px solid var(--line);width:250px;padding-bottom:8px;margin-bottom:12px}
.col li{font-size:11px;color:#555;line-height:2.45;padding-left:18px;position:relative}
.col li:before{content:"";position:absolute;left:4px;top:11px;width:4px;height:4px;border-right:1.2px solid #777;border-top:1.2px solid #777;transform:rotate(45deg)}
.site-footer{position:absolute;left:0;top:3334px;width:1200px;height:286px;background:var(--dark);color:#bbb;display:flex;padding:40px 0 0 68px}
.fcol{width:245px}
.fcol h6{font-size:12px;color:#fff;font-weight:700;margin-bottom:12px}
.fcol li{font-size:11px;line-height:1.7}
.fcol h6.second{margin-top:30px}
.social{display:flex;gap:16px;margin:6px 0 28px}
.social i{display:block;width:24px;height:24px;border-radius:50%;background:#ddd}
.newsletter{display:flex;margin-top:10px}
.newsletter .in{width:175px;height:28px;background:#fff;font-size:10px;color:#999;display:flex;align-items:center;padding-left:8px}
.newsletter .sub{width:85px;height:28px;background:var(--orange);color:#fff;font-size:10px;font-weight:700;display:flex;align-items:center;justify-content:center}
.copy{position:absolute;left:0;top:3620px;width:1200px;height:24px;background:var(--darker);color:#aaa;font-size:11px;display:flex;align-items:center;justify-content:center}
</style>
</head>
<body>
<svg width="0" height="0" style="position:absolute">
  <defs>
    <symbol id="star" viewBox="0 0 20 20"><path d="M10 1l2.7 5.8 6.3.7-4.7 4.3 1.3 6.2L10 14.9 4.4 18l1.3-6.2L1 7.5l6.3-.7z"/></symbol>
  </defs>
</svg>

<div class="topbar">
  <div><span>Language ▾</span><span>Currency ▾</span></div>
  <div class="right"><span>? Help</span><span>♥ Favourite</span><span>● Log in</span></div>
</div>

<header class="site-header">
  <div class="logo">
    <div class="name"><i></i>uTrundle</div>
    <div class="tag">YOUR ADVENTURE STARTS HERE!</div>
  </div>
  <div class="search">
    <div class="select">Choose a destination</div>
    <div class="select">Choose an activity</div>
    <div class="go">LET'S GO!</div>
  </div>
</header>

<div class="page">
  <main class="main">
    <section class="product">
      <div class="product-photo" role="img" aria-label="Surfer riding a wave on a surfboard"></div>
      <div class="product-info">
        <h1 class="product-title">KITE SURF GROUP LESSON</h1>
        <div class="duration">3 DAYS</div>
        <p class="intro">Sure, everyone knows about the coffee shops – but what else is fun to do in Amsterdam? Holland's capital city is a hub for happy cyclists, lazy beers by the canal, and art-lovers. As you start planning what to see, here are ten activities you can't miss[...]</p>
        <div class="rating">
          <span class="stars"><svg><use href="#star"/></svg><svg><use href="#star"/></svg><svg><use href="#star"/></svg><svg><use href="#star"/></svg><svg><use href="#star"/></svg></span>
          1475 Reviews
        </div>
        <div class="price-row">
          <div><div class="from">from US</div><div class="price"><small>$</small>654.00</div></div>
          <div class="btn book">Book Now</div>
        </div>
      </div>
    </section>

    <div class="share">
      <b>Share On:</b>
      <span class="dot" style="background:#4a5f8f" aria-label="Share on social network"></span>
      <span class="dot" style="background:#3fa8dc" aria-label="Share on social network"></span>
      <span class="dot" style="background:#2f79a8" aria-label="Share on social network"></span>
      <span class="dot" style="background:#d3503c" aria-label="Share on social network"></span>
      <span class="dot" style="background:#3aa457" aria-label="Share"><svg viewBox="0 0 16 16"><circle cx="4" cy="8" r="2"/><circle cx="12" cy="3.5" r="2"/><circle cx="12" cy="12.5" r="2"/><path d="M6 7l4-2.5M6 9l4 2.5"/></svg></span>
      <span class="dot" style="background:#f39a1e" aria-label="Feed"><svg viewBox="0 0 16 16"><path d="M3 3a10 10 0 0 1 10 10M3 7a6 6 0 0 1 6 6"/><circle cx="4" cy="12" r="1" fill="#fff"/></svg></span>
      <span class="dot" style="background:#9a9a9a" aria-label="Email"><svg viewBox="0 0 16 16"><rect x="2" y="4" width="12" height="8"/><path d="M2 4l6 5 6-5"/></svg></span>
    </div>

    <ul class="tabs">
      <li class="active" style="width:118px">Description</li>
      <li style="width:176px">What's Included &amp; Not</li>
      <li style="width:162px">Important Notes</li>
      <li style="width:120px">Others</li>
      <li style="width:96px">Map</li>
    </ul>

    <div class="tab-panel">
      <h2 class="section-title">Description</h2>
      <p>Lorem ipsum dolor sit amet, consectetur adipiscing elit. Donec dignissim enim id ante convallis, quis pretium enim molestie. Oras et arcu dolor. Maecenas nisi nisl, ultrices ac posuere nec, euismod id lacus. Ut dictum hendrerit eleifend. Morbi mi tellus, feugiat fringilla feugiat porta, molestie eu neque.</p>
      <p>Phasellus sit amet orci quis massa gravida mollis ut mollis nibh. Sed sit amet egestas est, a tincidunt sem. Nulla tincidunt elit libero, a semper velit gravida id. Sed faucibus lorem quis sapien mattis, at tempor justo pretium. Pellentesque porttitor bibendum maximus. Mauris vitae tellus quis augue aliquam maximum. Sed vel lorem a lorem blandit tincidunt vel at nunc. Lorem ipsum dolor sit amet, consectetur adipiscing elit. Donec dignissim enim id ante convallis, quis pretium enim molestie. Oras et arcu dolor. Maecenas nisi nisl, ultrices ac posuere nec, euismod id lacus. Ut dictum hendrerit eleifend. Morbi mi tellus, feugiat fringilla feugiat porta, molestie eu neque.</p>
      <p>Phasellus sit amet orci quis massa gravida mollis ut mollis nibh. Sed sit amet egestas est, a tincidunt sem. Nulla tincidunt elit libero, a semper velit gravida id. Sed faucibus lorem quis sapien mattis, at tempor justo pretium. Pellentesque porttitor bibendum maximus. Mauris vitae tellus quis augue aliquam maximum. Sed vel lorem a lorem blandit tincidunt vel at nunc.</p>

      <div class="block">
        <h2 class="section-title">What's Included &amp; Not</h2>
        <div class="group">Price includes :</div>
        <ul class="bullets">
          <li>Lorem ipsum dolor sit amet, consectetur adipiscing elit.</li>
          <li>Quisque non nisi sed erat lobortis feugiat vitae sed lacus.</li>
          <li>Fusce non ante in nulla feugiat imperdiet in id sem.</li>
          <li>In ultricies augue vel velit dictum, ac aliquam magna congue.</li>
        </ul>
        <div class="group">Price does not included :</div>
        <ul class="bullets">
          <li>Lorem ipsum dolor sit amet, consectetur adipiscing elit.</li>
          <li>Quisque non nisi sed erat lobortis feugiat vitae sed lacus.</li>
          <li>Fusce non ante in nulla feugiat imperdiet in id sem.</li>
        </ul>
      </div>

      <div class="block">
        <h2 class="section-title">Important Notes</h2>
        <div class="group">Prerequisites :</div>
        <ul class="bullets">
          <li>Lorem ipsum dolor sit amet, consectetur adipiscing elit.</li>
          <li>Quisque non nisi sed erat lobortis feugiat vitae sed lacus.</li>
          <li>Fusce non ante in nulla feugiat imperdiet in id sem.</li>
          <li>In ultricies augue vel velit dictum, ac aliquam magna congue.</li>
        </ul>
        <div class="group">Please bring :</div>
        <ul class="bullets">
          <li>Lorem ipsum dolor sit amet, consectetur adipiscing elit.</li>
          <li>Quisque non nisi sed erat lobortis feugiat vitae sed lacus.</li>
          <li>Fusce non ante in nulla feugiat imperdiet in id sem.</li>
        </ul>
      </div>

      <div class="block">
        <h2 class="section-title">Others</h2>
        <p>Lorem ipsum dolor sit amet, consectetur adipiscing elit. Quisque non nisi sed erat lobortis feugiat vitae sed lacus. Fusce non ante in nulla feugiat imperdiet in id sem. In ultricies augue vel velit dictum, ac aliquam magna congue.</p>
      </div>

      <div class="block" style="margin-top:20px">
        <h2 class="section-title">Map</h2>
        <div class="map" role="img" aria-label="Street map showing the activity meeting point"></div>
      </div>
    </div>

    <section class="reviews">
      <div class="reviews-head">
        <h3>What Other People Are Saying <small>(1465 reviews)</small></h3>
        <div class="filter">Filter By rating <div class="select">see all reviews</div></div>
      </div>
      <div class="review">
        <h4>“GREAT TOUR”</h4>
        <span class="stars"><svg><use href="#star"/></svg><svg><use href="#star"/></svg><svg><use href="#star"/></svg><svg><use href="#star"/></svg><svg><use href="#star"/></svg></span>
        <div class="body">Good visit, nice art, good cafe.</div>
        <div class="by">Reviewed By</div><div class="who">FindMyOuting Customer (United States)</div>
        <div class="date">November 27, 2015</div>
        <div class="helpful">was this helpful? <span class="yes">Yes</span></div>
      </div>
      <div class="review">
        <h4>“GREAT TOUR”</h4>
        <span class="stars"><svg><use href="#star"/></svg><svg><use href="#star"/></svg><svg><use href="#star"/></svg><svg><use href="#star"/></svg><svg><use href="#star"/></svg></span>
        <div class="body">Good visit, nice art, good cafe.</div>
        <div class="by">Reviewed By</div><div class="who">FindMyOuting Customer (United States)</div>
        <div class="date">November 27, 2015</div>
        <div class="helpful">was this helpful? <span class="yes">Yes</span></div>
      </div>
      <div class="review">
        <h4>“GREAT TOUR”</h4>
        <span class="stars"><svg><use href="#star"/></svg><svg><use href="#star"/></svg><svg><use href="#star"/></svg><svg><use href="#star"/></svg><svg><use href="#star"/></svg></span>
        <div class="body">Good visit, nice art, good cafe.</div>
        <div class="by">Reviewed By</div><div class="who">FindMyOuting Customer (United States)</div>
        <div class="date">November 27, 2015</div>
        <div class="helpful">was this helpful? <span class="yes">Yes</span></div>
      </div>
      <div class="review" style="border-bottom:0">
        <h4>“GREAT TOUR”</h4>
        <span class="stars"><svg><use href="#star"/></svg><svg><use href="#star"/></svg><svg><use href="#star"/></svg><svg><use href="#star"/></svg><svg><use href="#star"/></svg></span>
        <div class="body">Good visit, nice art, good cafe.</div>
        <div class="by">Reviewed By</div><div class="who">FindMyOuting Customer (United States)</div>
        <div class="date">November 27, 2015</div>
        <div class="helpful">was this helpful? <span class="yes">Yes</span></div>
      </div>
      <div class="btn more-review" style="margin-top:0">Show More Review</div>
    </section>
  </main>

  <aside class="aside">
    <section class="calendar">
      <div class="cal-head">Booking Calendar</div>
      <div class="step">
        <div class="label"><span class="num">1</span>Select Travel Date</div>
        <div class="fields"><div class="mini">1 ▾</div><div class="mini">Dec 2015 ▾</div>
          <svg width="20" height="20" viewBox="0 0 20 20"><rect x="2" y="4" width="16" height="14" fill="#2f79a8"/><rect x="4" y="8" width="12" height="8" fill="#fff"/><rect x="5" y="2" width="2" height="4" fill="#2f79a8"/><rect x="13" y="2" width="2" height="4" fill="#2f79a8"/></svg></div>
        <div class="hint">FLEXIBLE DATE GUARANTEE ▸</div>
      </div>
      <div class="divider"></div>
      <div class="step">
        <div class="label"><span class="num">2</span>Enter Total Number of Travelers</div>
        <div class="travellers">
          <div>Adult (Age 3+) <span class="mini">0 ⇕</span></div>
          <div>Infant (Age 0 to 2) <span class="mini">0 ⇕</span></div>
        </div>
        <div class="hint" style="font-weight:400">What's this, and can I change it? ▾</div>
      </div>
      <div class="btn check">Check Availability</div>
    </section>

    <section class="aside-reviews">
      <div class="rev-head">
        <svg width="250" height="62" viewBox="0 0 250 62"><path d="M0 0h250v46l-125 16L0 46z" fill="var(--magenta)"/></svg>
        <span>REVIEWS</span>
      </div>
      <div class="mini-review">
        <h5>GOOD VISIT</h5>
        <span class="stars"><svg><use href="#star"/></svg><svg><use href="#star"/></svg><svg><use href="#star"/></svg><svg><use href="#star"/></svg><svg><use href="#star"/></svg></span>
        <p>Good visit, nice art, good cafe.</p>
        <div class="from-line">From Jack Dalton(United States) on<br><em>November 27, 2015</em></div>
      </div>
      <div class="mini-review">
        <h5>GOOD VISIT</h5>
        <span class="stars"><svg><use href="#star"/></svg><svg><use href="#star"/></svg><svg><use href="#star"/></svg><svg><use href="#star"/></svg><svg><use href="#star"/></svg></span>
        <p>Good visit, nice art, good cafe.</p>
        <div class="from-line">From Jack Dalton(United States) on<br><em>November 27, 2015</em></div>
      </div>
      <div class="mini-review">
        <h5>GOOD VISIT</h5>
        <span class="stars"><svg><use href="#star"/></svg><svg><use href="#star"/></svg><svg><use href="#star"/></svg><svg><use href="#star"/></svg><svg><use href="#star"/></svg></span>
        <p>Good visit, nice art, good cafe.</p>
        <div class="from-line">From Jack Dalton(United States) on<br><em>November 27, 2015</em></div>
      </div>
      <div class="mini-review" style="border-bottom:0">
        <h5>“GOOD VISIT”</h5>
        <span class="stars"><svg><use href="#star"/></svg><svg><use href="#star"/></svg><svg><use href="#star"/></svg><svg><use href="#star"/></svg><svg><use href="#star"/></svg></span>
        <p>Good visit, nice art, good cafe.</p>
        <div class="from-line">From <em style="color:var(--magenta);font-style:italic">Jack Dalton (United States)</em> on <em>November 27, 2015</em></div>
      </div>
      <div class="btn see-all" style="margin-top:0">See All Reviews</div>
    </section>

    <div class="offer">
      <div class="offer-photo" role="img" aria-label="Wooden cabin by a lake with mountains"></div>
      <div class="heart"><svg viewBox="0 0 20 20"><path d="M10 17l-7-7a4 4 0 0 1 7-4 4 4 0 0 1 7 4z"/></svg></div>
      <div class="offer-body">Amsterdam: 1.5-Hour Evening Canal Cruise
        <div class="offer-foot"><div><span class="stars"><svg><use href="#star"/></svg><svg><use href="#star"/></svg><svg><use href="#star"/></svg><svg><use href="#star"/></svg><svg><use href="#star"/></svg></span><div class="count">1465 Review</div></div><div class="amt">From<b>US$ 16</b></div></div>
      </div>
    </div>
    <div class="offer">
      <div class="offer-photo" role="img" aria-label="Wooden cabin by a lake with mountains"></div>
      <div class="heart"><svg viewBox="0 0 20 20"><path d="M10 17l-7-7a4 4 0 0 1 7-4 4 4 0 0 1 7 4z"/></svg></div>
      <div class="offer-body">Amsterdam: 1.5-Hour Evening Canal Cruise
        <div class="offer-foot"><div><span class="stars"><svg><use href="#star"/></svg><svg><use href="#star"/></svg><svg><use href="#star"/></svg><svg><use href="#star"/></svg><svg><use href="#star"/></svg></span><div class="count">1465 Review</div></div><div class="amt">From<b>US$ 16</b></div></div>
      </div>
    </div>
    <div class="offer">
      <div class="offer-photo" role="img" aria-label="Wooden cabin by a lake with mountains"></div>
      <div class="heart"><svg viewBox="0 0 20 20"><path d="M10 17l-7-7a4 4 0 0 1 7-4 4 4 0 0 1 7 4z"/></svg></div>
      <div class="offer-body">Amsterdam: 1.5-Hour Evening Canal Cruise
        <div class="offer-foot"><div><span class="stars"><svg><use href="#star"/></svg><svg><use href="#star"/></svg><svg><use href="#star"/></svg><svg><use href="#star"/></svg><svg><use href="#star"/></svg></span><div class="count">1465 Review</div></div><div class="amt">From<b>US$ 16</b></div></div>
      </div>
    </div>
    <div class="offer">
      <div class="offer-photo" role="img" aria-label="Wooden cabin by a lake with mountains"></div>
      <div class="heart"><svg viewBox="0 0 20 20"><path d="M10 17l-7-7a4 4 0 0 1 7-4 4 4 0 0 1 7 4z"/></svg></div>
      <div class="offer-body">Amsterdam: 1.5-Hour Evening Canal Cruise
        <div class="offer-foot"><div><span class="stars"><svg><use href="#star"/></svg><svg><use href="#star"/></svg><svg><use href="#star"/></svg><svg><use href="#star"/></svg><svg><use href="#star"/></svg></span><div class="count">1465 Review</div></div><div class="amt">From<b>US$ 16</b></div></div>
      </div>
    </div>
    <div class="offer">
      <div class="offer-photo" role="img" aria-label="Wooden cabin by a lake with mountains"></div>
      <div class="heart"><svg viewBox="0 0 20 20"><path d="M10 17l-7-7a4 4 0 0 1 7-4 4 4 0 0 1 7 4z"/></svg></div>
      <div class="offer-body">Amsterdam: 1.5-Hour Evening Canal Cruise
        <div class="offer-foot"><div><span class="stars"><svg><use href="#star"/></svg><svg><use href="#star"/></svg><svg><use href="#star"/></svg><svg><use href="#star"/></svg><svg><use href="#star"/></svg></span><div class="count">1465 Review</div></div><div class="amt">From<b>US$ 16</b></div></div>
      </div>
    </div>
    <div class="btn more-offer">Show More Offer</div>
  </aside>
</div>

<section class="footer-links">
  <div class="col"><h6>Top Destinations</h6><ul>
    <li>San Juan: Tours &amp; Tickets online</li><li>Barcelona: Tours &amp; Tickets online</li><li>New York: Tours &amp; Tickets online</li><li>Reykjavik: Tours &amp; Tickets online</li><li>Amsterdam: Tours &amp; Tickets online</li><li>Zadar: Tours &amp; Tickets online</li><li>Jerusalem: Tours &amp; Tickets online</li><li>Sydney: Tours &amp; Tickets online</li></ul></div>
  <div class="col"><h6>Popular on uTrundle</h6><ul>
    <li>Paris Dinner &amp; Lunch Cruises</li><li>Dubai Quad &amp; ATV Tours</li><li>Rome Hop-on Hop-off Tours</li><li>Rome E-Glider Tours</li><li>London Wizard Film Tours</li><li>Barcelona E-Glider Tours</li><li>San Francisco E-Glider Tours</li><li>Mykonos Sailing Trips &amp; Boat Tours</li></ul></div>
  <div class="col"><h6>Popular Attractions</h6><ul>
    <li>Eiffel Tower: Tours &amp; Tickets online</li><li>Film Studio Backlot: Tours &amp; Tickets online</li><li>Alhambra: Tours &amp; Tickets online</li><li>Burj Khalifa: Tours &amp; Tickets online</li><li>Doge's Palace: Tours &amp; Tickets online</li><li>Hermitage Museum: Tours &amp; Tickets online</li><li>Colosseum: Tours &amp; Tickets online</li><li>Canal House Museum: Tours &amp; Tickets online</li></ul></div>
</section>

<footer class="site-footer">
  <div class="fcol"><h6>COMPANY</h6><ul><li>About uTrundle.net</li><li>corporate Info</li><li>Site map</li><li>Blog</li><li>Careers</li></ul></div>
  <div class="fcol"><h6>SUPPORT</h6><ul><li>Contact Us</li><li>FAQs</li></ul><h6 class="second">T &amp; C</h6><ul><li>Privacy Policy</li><li>Legal</li></ul></div>
  <div class="fcol"><h6>PARTNERSHIPS</h6><ul><li>Supplier Sign up</li><li>Affiliate Programs</li></ul><h6 class="second">LOG-INS</h6><ul><li>Customers</li><li>Suppliers</li></ul></div>
  <div class="fcol"><h6>BE SOCIALS</h6>
    <div class="social"><i></i><i></i><i></i><i></i><i></i><i></i></div>
    <h6>SUBSCRIBE NEWSLETTERS</h6>
    <div class="newsletter"><div class="in">your email id</div><div class="sub">SUBSCRIBE</div></div>
  </div>
</footer>
<div class="copy">© 2015, All Rights Reserved, uTrundle.net</div>
</body>
</html>
```